New Flyer Design Project

I have an Upmarket Hair and Beauty Salon near the beach. I already have a current logo but it needs to change to Hair AND Beauty as we were only doing beauty. I want it to have a special on the flyer and to be DL size. I like it to be elegant with soft colours. I like the blues/teals also. I have attached the current business cards. I want it to tie in with the business cards somehow as well. I want the add to have something along the lines of - Marlow & Tess now introduce to you Hair AND Beauty. We have combined our team to offer you all of your hair and beauty needs in the one great location! NEW CLIENTS OFFER $49 Style Cut & Blowdry and 30% off ALL Waxing

We are a Velunique and Sorvantica Salon so you can google to get the feel of the brand. The flyer will be used as a leaflet drop.
Please include an expiry of march 31st 2015
I would prefer not to use stock images also
Phone Number 08 9274 3185
shop 2&3 Warrick cove Pde
Yanchep 6035

Thankyou :)

Target Market(s)

20-40

Industry/Entity Type

Hair

Requirements
Must have
• DL size
Address & Contact details
08 9274 3185
shop 2&3 Warrick Cove Pde
Yanchep 6053
Should not have
• Do not like clip arts-scissors etc
Would prefer not to use stock images

```html
<!DOCTYPE html>
<html lang="en">
<head>
<meta charset="utf-8">
<title>Marlow &amp; Tess – New Clients Offer</title>
<link href="https://fonts.googleapis.com/css2?family=Comfortaa:wght@300;400&family=Open+Sans:ital,wght@0,400;0,700;1,700;1,800&family=Old+Standard+TT:wght@400;700&family=Roboto+Condensed:wght@400;700&family=Libre+Baskerville&display=swap" rel="stylesheet">
<style>
  :root {
    --slate-dark: #3a404c;
    --slate-mid: #474e5c;
    --teal: #4fd1c5;
    --white: #ffffff;
    --brown: #6b5440;
    --gold: #b8956a;
    --sky: #3fbfe9;
    --sky-light: #63d0f3;
    --plum: #8e2a8c;
    --orange: #f7941d;
  }
  html, body {
    margin: 0;
    padding: 0;
    width: 848px;
    height: 1200px;
    overflow: hidden;
    background: #efefef;
  }
  .flyer {
    position: relative;
    width: 848px;
    height: 1200px;
    overflow: hidden;
    background: var(--slate-dark);
    color: var(--white);
  }
  .flyer__backdrop {
    position: absolute;
    inset: 0;
  }
  .flyer__text {
    position: absolute;
    margin: 0;
    line-height: 1;
    white-space: nowrap;
  }
  .brand-box {
    position: absolute;
    left: 35px;
    top: 26px;
    width: 437px;
    height: 103px;
    background: var(--white);
    border: 2px solid var(--gold);
    box-sizing: border-box;
    display: flex;
    align-items: center;
    justify-content: center;
  }
  .brand-box__name {
    margin: 0;
    font-family: "Libre Baskerville", serif;
    font-size: 48px;
    line-height: 1;
    color: var(--brown);
  }
  .intro {
    left: 42px;
    top: 160px;
    font-family: "Comfortaa", sans-serif;
    font-weight: 300;
    font-style: italic;
    font-size: 29px;
    line-height: 38px;
    color: var(--teal);
  }
  .headline {
    left: 37px;
    top: 404px;
    font-family: "Open Sans", sans-serif;
    font-weight: 800;
    font-style: italic;
    font-size: 45px;
    line-height: 58px;
    letter-spacing: -0.5px;
  }
  .offer-kicker {
    left: 304px;
    top: 597px;
    font-family: "Old Standard TT", serif;
    font-size: 33px;
  }
  .offer-title {
    left: 280px;
    top: 626px;
    font-family: "Old Standard TT", serif;
    font-weight: 700;
    font-size: 80px;
    letter-spacing: 1px;
  }
  .deal {
    position: absolute;
    top: 718px;
    font-family: "Old Standard TT", serif;
  }
  .deal--cut { left: 168px; }
  .deal--wax { left: 467px; }
  .deal__figure {
    margin: 0;
    font-size: 88px;
    line-height: 80px;
    font-weight: 700;
  }
  .deal__label {
    margin: 6px 0 0;
    font-size: 36px;
    line-height: 40px;
    letter-spacing: 0.5px;
  }
  .promo-band {
    position: absolute;
    left: 0;
    top: 941px;
    width: 848px;
    height: 75px;
    background: linear-gradient(180deg, var(--sky-light), var(--sky));
  }
  .promo-band__text {
    margin: 0;
    padding: 12px 0 0 37px;
    font-family: "Open Sans", sans-serif;
    font-weight: 700;
    font-style: italic;
    font-size: 20px;
    line-height: 27px;
  }
  .contact-email {
    left: 35px;
    top: 1055px;
    font-family: "Open Sans", sans-serif;
    font-size: 18px;
  }
  .contact-phone {
    left: 33px;
    top: 1080px;
    font-family: "Open Sans", sans-serif;
    font-weight: 700;
    font-size: 48px;
    letter-spacing: -0.5px;
  }
  .contact-address {
    left: 35px;
    top: 1141px;
    font-family: "Open Sans", sans-serif;
    font-size: 19px;
  }
  .expiry-badge {
    position: absolute;
    left: 612px;
    top: 960px;
    width: 176px;
    height: 176px;
  }
  .expiry-badge__text {
    position: absolute;
    inset: 0;
    margin: 0;
    padding-top: 34px;
    text-align: center;
    font-family: "Roboto Condensed", sans-serif;
    font-size: 26px;
    line-height: 28px;
    color: var(--white);
  }
  .expiry-badge__year {
    display: block;
    margin-top: 4px;
    font-weight: 700;
    font-size: 40px;
    line-height: 40px;
    color: var(--orange);
  }
</style>
</head>
<body>
<main class="flyer">
  <svg class="flyer__backdrop" width="848" height="1200" viewBox="0 0 848 1200">
    <defs>
      <linearGradient id="portraitTone" x1="0" y1="0" x2="0.35" y2="1">
        <stop offset="0" stop-color="#ffffff"/>
        <stop offset="0.3" stop-color="#f6d8c2"/>
        <stop offset="0.55" stop-color="#d97fb4"/>
        <stop offset="0.75" stop-color="#b552a8"/>
        <stop offset="1" stop-color="#5b86d2"/>
      </linearGradient>
      <linearGradient id="coolEdge" x1="0" y1="0" x2="1" y2="0.3">
        <stop offset="0.5" stop-color="#79b4df" stop-opacity="0"/>
        <stop offset="1" stop-color="#79b4df" stop-opacity="0.55"/>
      </linearGradient>
    </defs>
    <g role="img" aria-label="Portrait area: soft-lit woman with a white lily in her hair on a pastel peach, pink and blue glow">
      <rect x="300" y="0" width="548" height="1200" fill="url(#portraitTone)"/>
      <rect x="300" y="0" width="548" height="1200" fill="url(#coolEdge)"/>
    </g>
    <polygon points="0,0 449,0 328,502 440,937 522,1200 0,1200" fill="var(--slate-mid)"/>
    <polygon points="0,0 410,0 300,500 408,937 418,1200 0,1200" fill="var(--slate-dark)"/>
  </svg>

  <header class="brand-box">
    <p class="brand-box__name">Marlow &amp; Tess</p>
  </header>

  <p class="flyer__text intro">We are a Velunique and<br>Sorvantica Salon so<br>you can google to get<br>the feel of the brand</p>

  <h1 class="flyer__text headline">WE introduce to<br>you Hair care &amp;<br>Beauty</h1>

  <p class="flyer__text offer-kicker">NEW CLIENTS</p>
  <p class="flyer__text offer-title">OFFER</p>

  <section class="deal deal--cut">
    <p class="deal__figure">$49</p>
    <p class="deal__label">STYLE CUT<br>&amp; BLOWDRY</p>
  </section>
  <section class="deal deal--wax">
    <p class="deal__figure">30%</p>
    <p class="deal__label">OFF ALL<br>WAXING</p>
  </section>

  <div class="promo-band">
    <p class="promo-band__text">We have combined our team to offer you all of your hair<br>and beauty needs in the one great location.</p>
  </div>

  <p class="flyer__text contact-email">marlow.tess.beauty@tessmail.com</p>
  <p class="flyer__text contact-phone">08 9274 3185</p>
  <p class="flyer__text contact-address">shop 4&amp;5 Warrick Cove Pde Seabrook 6048</p>

  <div class="expiry-badge">
    <svg width="176" height="176" viewBox="0 0 176 176">
      <circle cx="88" cy="88" r="85" fill="var(--white)"/>
      <circle cx="88" cy="88" r="80" fill="var(--plum)" stroke="var(--white)" stroke-width="4" stroke-dasharray="6 4"/>
    </svg>
    <p class="expiry-badge__text">EXPIRY OF<br>MARCH<br>31ST<span class="expiry-badge__year">2015</span></p>
  </div>
</main>
</body>
</html>
```